Geschäftspapiere Campingplatz
Zielgruppe
Campingplatz
Aufgabenstellung
Geschäftspapiere, Briefpapier, Visitenkarte, Briefumschlag und DIN A5 Memoblock farblich und designmäßig am Logo orientiert.
Memoblock sollte sich vom Briefpapier unterscheiden und nicht so viele Daten enthalten.
Website, E-Mail, Telefonnummer, Festnetz, Adresse und Inhaber sollen auf dem Briefpapier erscheinen.
Auf der Visitenkarte soll nur statt Inhaber stehen und zusätzlich die Handynummer, sowie alle anderen Daten.
Die Datensätze sollten sich mit entsprechendem Programm von uns bearbeiten lassen.

```html
<!DOCTYPE html>
<html lang="de">
<head>
<meta charset="utf-8">
<title>Camping Talwiese – Briefpapier</title>
<link rel="stylesheet" href="https://fonts.googleapis.com/css2?family=Quicksand:wght@700&family=Source+Sans+3:wght@400;600&display=swap">
<style>
  :root {
    --backdrop: #2c3a4f;
    --paper: #f7f7f6;
    --brand-green: #8aa145;
    --band-green: #7e9c50;
    --ink: #3a3a3a;
    --ink-soft: #555;
    --white: #ffffff;
  }
  * { box-sizing: border-box; margin: 0; padding: 0; }
  html, body { width: 1200px; height: 800px; overflow: hidden; }
  body {
    background: var(--backdrop);
    font-family: "Source Sans 3", sans-serif;
    color: var(--ink);
  }
  .canvas { position: relative; width: 1200px; height: 800px; }

  .sheet {
    position: absolute;
    top: 89px;
    width: 440px;
    height: 622px;
    background: var(--paper);
    box-shadow: 0 10px 24px rgba(0,0,0,.35);
  }
  .sheet--blank { left: 125px; }
  .sheet--letter { left: 640px; }

  .brand {
    position: absolute;
    top: 22px;
    left: 0; right: 0;
    display: flex;
    justify-content: center;
    align-items: center;
    gap: 6px;
  }
  .brand__dot {
    width: 9px; height: 9px;
    border-radius: 50%;
    background: var(--brand-green);
  }
  .brand__name {
    font-family: "Source Sans 3", sans-serif;
    font-weight: 600;
    font-size: 17px;
    color: var(--brand-green);
    letter-spacing: .2px;
  }

  .header-rule {
    position: absolute;
    top: 56px; left: 34px; right: 34px;
    height: 1.5px;
    background: var(--brand-green);
  }

  .sender-line {
    position: absolute;
    top: 52px; left: 55px;
    width: 162px;
    padding-bottom: 2px;
    border-bottom: 1px solid #999;
    font-size: 5.4px;
    color: var(--ink-soft);
  }
  .address-zone {
    position: absolute;
    top: 97px; left: 55px;
    font-size: 5.6px;
  }
  .letter-body {
    position: absolute;
    top: 194px; left: 56px;
    width: 342px;
    font-size: 5.4px;
    line-height: 1.45;
    text-align: justify;
  }
  .letter-body p { margin-bottom: 5px; }
  .letter-body .salutation { margin-bottom: 6px; }
  .closing {
    position: absolute;
    top: 360px; left: 57px;
    font-size: 5.6px;
  }
  .closing p + p { margin-top: 8px; }

  .footer-band {
    position: absolute;
    left: 0; right: 0; bottom: 0;
    height: 72px;
    background: var(--band-green);
    color: var(--white);
    display: flex;
    justify-content: space-between;
  }
  .footer-band--large { padding: 12px 30px 0 30px; font-size: 8.4px; letter-spacing: .6px; line-height: 1.3; }
  .footer-band--large .footer__company { font-weight: 600; margin-top: 4px; margin-bottom: 11px; }
  .footer-band--large .footer__contact { text-align: right; }
  .footer-band--large .footer__email { margin-bottom: 10px; }

  .footer-band--small { padding: 10px 40px 0 42px; font-size: 5.3px; line-height: 1.4; }
  .footer-band--small .footer__company { font-weight: 600; margin-top: 3px; margin-bottom: 8px; }
  .footer-band--small .footer__owner { font-weight: 600; }
  .footer-band--small .footer__contact { text-align: right; }
  .footer-band--small .footer__email { margin-bottom: 7px; }
</style>
</head>
<body>
<main class="canvas">

  <section class="sheet sheet--blank" aria-label="Briefbogen ohne Text">
    <div class="brand">
      <span class="brand__dot"></span>
      <span class="brand__name">Camping Talwiese</span>
    </div>
    <div class="header-rule"></div>
    <footer class="footer-band footer-band--large">
      <div class="footer__address">
        <p class="footer__company">Camping Talwiese</p>
        <p>Wiesenweg 12</p>
        <p>57399 Grünhofen</p>
      </div>
      <div class="footer__contact">
        <p class="footer__email">info@camping-talwiese.de</p>
        <p>www.camping-talwiese.de</p>
        <p>Telefon: +49 12345678</p>
        <p>Telefax: +49 1234567890</p>
      </div>
    </footer>
  </section>

  <section class="sheet sheet--letter" aria-label="Briefbogen mit Mustertext">
    <div class="brand">
      <span class="brand__dot"></span>
      <span class="brand__name">Camping Talwiese</span>
    </div>
    <p class="sender-line">Marlene Voss,&nbsp; Wiesenweg 12 57399 Grünhofen</p>
    <p class="address-zone">Anschriftzone</p>

    <div class="letter-body">
      <p class="salutation">Sehr geehrte Damen und Herren,</p>
      <p>Wir danken Ihnen für Ihre Anfrage und freuen uns über Ihr Interesse an unserem Platz. Gern senden wir Ihnen die aktuellen Preise für Stellplätze, Mietzelte und Wohnwagen zu. In der Vorsaison gelten ermäßigte Tarife, Familien erhalten zudem einen Nachlass ab der dritten Nacht. Strom, Wasser und Duschen sind im Preis bereits enthalten, Haustiere sind nach Absprache herzlich willkommen.</p>
      <p>Haben Sie noch Fragen zur Anreise?<br>Unsere Rezeption ist täglich von acht bis zwanzig Uhr besetzt. Bitte teilen Sie uns Ihren Ankunftstag mit, damit wir Ihren Platz am Ufer reservieren können. Die Bestätigung erhalten Sie per E-Mail.</p>
      <p>Wir freuen uns darauf, Sie bald bei uns begrüßen zu dürfen, und wünschen Ihnen schon jetzt eine gute Reise.</p>
    </div>

    <div class="closing">
      <p>Mit freundlichen Grüßen,</p>
      <p>Marlene Voss</p>
    </div>

    <footer class="footer-band footer-band--small">
      <div class="footer__address">
        <p class="footer__company">Camping Talwiese</p>
        <p class="footer__owner">Inhaberin: Marlene Voss</p>
        <p>Wiesenweg 12</p>
        <p>57399 Grünhofen</p>
      </div>
      <div class="footer__contact">
        <p class="footer__email">info@camping-talwiese.de</p>
        <p>www.camping-talwiese.de</p>
        <p>Telefon: +49 12345678</p>
        <p>Telefax: +49 1234567890</p>
      </div>
    </footer>
  </section>

</main>
</body>
</html>
```